Business cards and stationary for zombie fantasy camp
The Bramble Lodge
Business cards and stationary for zombie fantasy camp - Outdoors
Creative Brief
Simple
Dwight Palmer
2648 Wendel Rd Fernwick Mt 59871
Dwight@thebramblelodge.example
www.thebramblelodge.example
Please refer to the website to get ideas as to what to add to this business card. I would like a design that speaks to the nature of the business. I have also uploaded 4 different logo's that I use, please feel free to experiment with each one. I'm in need of business cards, stationary, presentation folders, etc...
Please refer to the website to get ideas as to what to add to this business card. I would like a design that speaks to the nature of the business.
Tovick88 Tovick88
Attention please all designers: I've extended this contest for 3 days, not so much to find new designs but many of you have submitted designs that are nearing what I'm looking for. And the three days will enable us all time to communicate and work through those changes. I don't want any of you missing out because I didn't get online until only the final hours risking being able to give you all a chance to make those modifications I'm looking for. Sorry for the delay, But, thank you for your patience and all of your work.
All designers please note, you each that have submitted ideas have some excellent business card ideas, There is only 1 day left, please stop concentrating on business cards, and start focusing on stationary, letterheads, envelopes, and email signatures, I'm looking for the whole package here.
Just a quick message to thank everyone for the work that they have put into my project, I've got some excellent designs. With that being said, I still would like to see more designs for items specifically with Presentation Folders, Stationary, envelopes, and email signatures
Feel free to use any logo that I have uploaded here. I like all of them, so I look forward to seeing what you can do with any one of them or all of them.
My project had started once before, quillhaven had noticed that I had a logo project running at the same time, so they made the recommendation to put this on hold until that project finished. To the designers that submitted already, I apologize to you all. The logo project is now finished, I had multiple logo's I likes so I've posted them here for you to use as your inspiration. Good luck to you all and with all projects, I look forward to seeing your work.
I will be looking to use these designs when ordering business cards through prenta nook.example, I'm also looking for designs for stationary, envelopes and presentation folders all ordered through prentanook.example

```html
<!DOCTYPE html>
<html lang="en">
<head>
<meta charset="utf-8">
<title>The Bramble Lodge — Business Card</title>
<link href="https://fonts.googleapis.com/css2?family=Oswald:wght@600&family=Roboto+Condensed:wght@300;400&display=swap" rel="stylesheet">
<style>
  :root {
    --page: #e9e6e0;
    --card-dark: #232323;
    --card-deep: #161616;
    --frame-grey: #5a5a5a;
    --brand-yellow: #e7b422;
    --text-light: #e6e6e6;
    --text-muted: #bdbdbd;
    --shade-warm: #3a3428;
  }
  * { margin: 0; padding: 0; box-sizing: border-box; }
  html, body { width: 1200px; height: 1023px; overflow: hidden; background: var(--page); }
  .stage { position: relative; width: 1200px; height: 1023px; }
  .card {
    position: absolute; left: 250px; width: 700px; height: 400px;
    background: linear-gradient(135deg, var(--card-dark), var(--card-deep));
    border-radius: 6px; overflow: hidden;
    box-shadow: 0 8px 24px rgba(0,0,0,.25);
  }
  .card-front { top: 70px; }
  .card-back { top: 553px; }

  /* front */
  .logo-frame {
    position: absolute; left: 40px; top: 80px; width: 270px; height: 250px;
    border: 6px solid var(--frame-grey); border-radius: 30px;
    display: flex; align-items: center; justify-content: center;
    padding: 0 16px;
  }
  .brand-name {
    font-family: "Oswald", sans-serif; font-weight: 600; color: var(--brand-yellow);
    font-size: 40px; line-height: 1.05; text-transform: uppercase; text-align: center;
  }
  .contact {
    position: absolute; left: 350px; top: 40px; width: 290px;
    border-left: 2px solid var(--brand-yellow); padding-left: 14px;
    font-family: "Roboto Condensed", sans-serif; color: var(--text-light);
  }
  .contact-name { font-size: 26px; font-weight: 400; margin-bottom: 22px; }
  .contact-line { font-size: 15px; font-weight: 300; color: var(--text-muted); line-height: 1.5; display: flex; align-items: center; gap: 8px; white-space: nowrap; }
  .contact-address { margin-bottom: 12px; display: block; }
  .contact-line svg { flex: none; }
  .edge-band {
    position: absolute; right: 0; top: 0; width: 44px; height: 100%;
    background: var(--brand-yellow);
    display: flex; align-items: center; justify-content: center;
  }
  .edge-band span {
    writing-mode: vertical-rl; transform: rotate(180deg);
    font-family: "Roboto Condensed", sans-serif; font-size: 13px; color: var(--card-deep); letter-spacing: .5px;
  }

  /* back */
  .back-art {
    position: absolute; inset: 0;
    background: radial-gradient(ellipse at 25% 30%, var(--shade-warm) 0%, transparent 45%),
                radial-gradient(ellipse at 75% 80%, var(--shade-warm) 0%, transparent 40%);
    opacity: .8;
  }
  .back-brand {
    position: absolute; inset: 0; display: flex; align-items: center; justify-content: center; gap: 14px;
  }
  .back-brand .brand-name { font-size: 48px; }
  .brand-dot { width: 18px; height: 18px; border-radius: 50%; background: var(--brand-yellow); flex: none; }
</style>
</head>
<body>
<main class="stage">
  <section class="card card-front">
    <div class="logo-frame">
      <span class="brand-name">The Bramble Lodge</span>
    </div>
    <div class="contact">
      <p class="contact-name">Dwight Palmer</p>
      <p class="contact-line contact-address">2648 Wendel Rd<br>Fernwick Mt 59871</p>
      <p class="contact-line">
        <svg width="12" height="12" viewBox="0 0 12 12"><rect width="12" height="12" rx="2" fill="#e7b422"/><path d="M3.5 2.5l1.5 0 .6 2-1 .8a5 5 0 0 0 2.1 2.1l.8-1 2 .6v1.5a1 1 0 0 1-1 1A6.5 6.5 0 0 1 2.5 3.5a1 1 0 0 1 1-1z" fill="#161616"/></svg>
        406.555.0148
      </p>
      <p class="contact-line">
        <svg width="12" height="12" viewBox="0 0 12 12"><rect width="12" height="12" rx="2" fill="#e7b422"/><rect x="2.5" y="3.5" width="7" height="5" fill="none" stroke="#161616"/><path d="M2.5 3.5l3.5 3 3.5-3" fill="none" stroke="#161616"/></svg>
        Dwight@thebramblelodge.example
      </p>
    </div>
    <div class="edge-band"><span>www.thebramblelodge.example</span></div>
  </section>

  <section class="card card-back">
    <div class="back-art" role="img" aria-label="Faint dark silhouettes of figures and bare branches across the card"></div>
    <div class="back-brand">
      <span class="brand-dot"></span>
      <span class="brand-name">The Bramble Lodge</span>
    </div>
  </section>
</main>
</body>
</html>
```